"Outside the Box" Newsletter Design Project-Communications Company

I am looking for an Internal newsletter for a communications company that will be sent to our sales and leadership team.
This newsletter will deliver forecasting, sales results, stack rankings for the sales reps, total team results, corporate updates, success stories and updates from Training/Operations/Sales/Marketing (could be a box for each)I would also need a couple sections with a blank header and box to add info as needed, if something comes up that is not set in stone weekly.
I am looking for a template that looks sharp and professional that i can use every week by just dropping content in, (text and possibly an employee picture) I will need it in a format (possibly word) that the will keep the text in line when I drop it in each week. Once complete I can save to a pdf and would like to have the ability to drop it into the body of an email.

We have a racecar theme that we use when training our sales folks so we would like a little bit of that to the newsletter and also incorporate our color scheme from our company.

I would like four versions of the newsletter..all would match other than the title.
1. Week 1 title - Start your engines
2. Week 2 title - Looking for suggestions
3. Week 3 title - Looking for suggestions
4. Week 4 title - Approaching the finish line, this version would also include an employee spotlight, one seperate section.

If we could include a few pics around racing that would be good, not over the top, just a few to give it a little of that feel. Maybe a checkered flag with the QV logo on it, a racecar..anything else that may make sense.

I will attach our logo and our organization is called SMB (small/medium business) so that should also be placed on there somewhere. Final design would need to be two pages, sharp professional feel, my Vice President likes a very clean look, not too busy. I have also attached a sample newsletter from another group in our company, ours will not have as much content, we are much smaller but this is a sample (on a smaller scale)of what we are looking for. The company look and feel is what we want to follow. Thank you

Target Market(s)

Our Internal sales team.

Industry/Entity Type

Communications

Requirements
Must have
• Ability to update with my content without having things shift and fall out of line..format that will make that easy and then able to save to PDF..2 pages long.
Nice to have
• HTML template to match.

```html
<!DOCTYPE html>
<html lang="en">
<head>
<meta charset="utf-8">
<title>QV SMB Newsletter – December 20, 2012</title>
<link href="https://fonts.googleapis.com/css2?family=Open+Sans:wght@400;600;700&display=swap" rel="stylesheet">
<style>
  :root {
    --page-bg: #efefef;
    --brand-purple: #823b96;
    --header-rule: #9a5aab;
    --row-white: #ffffff;
    --row-alt: #f5f5f5;
    --row-rule: #e6e6e6;
    --text-main: #333333;
    --text-dark: #2b2b2b;
    --car-red: #d7261e;
    --car-dark: #8e1510;
  }
  * { box-sizing: border-box; margin: 0; padding: 0; }
  html, body { width: 940px; height: 1200px; overflow: hidden; }
  body {
    background: var(--page-bg);
    font-family: "Open Sans", Arial, sans-serif;
    color: var(--text-main);
    position: relative;
  }
  .masthead { position: absolute; left: 0; top: 0; width: 940px; height: 110px; }
  .masthead .car {
    position: absolute; top: 18px; width: 132px; height: 72px;
    border-radius: 30px 30px 14px 14px;
    background: linear-gradient(180deg, var(--car-red), var(--car-dark));
  }
  .masthead .car-left { left: 32px; }
  .masthead .car-right { left: 260px; }
  .masthead .brand-name {
    position: absolute; left: 176px; top: 24px; width: 78px; height: 60px;
    display: flex; align-items: center; justify-content: center;
    font-size: 19px; font-weight: 700; color: var(--text-dark);
  }
  .issue {
    position: absolute; right: 31px; top: 30px; text-align: right; color: var(--text-dark);
  }
  .issue-date { font-size: 19px; font-weight: 700; line-height: 26px; }
  .issue-date span { font-weight: 400; }
  .issue-title { font-size: 17px; line-height: 26px; }

  .board {
    position: absolute; left: 31px; width: 878px;
    border-collapse: collapse; table-layout: fixed;
    box-shadow: 0 1px 3px rgba(0,0,0,0.18);
  }
  .board th {
    background: var(--brand-purple); color: #fff;
    font-size: 15.5px; font-weight: 700; line-height: 29px;
    text-align: left; vertical-align: middle; height: 81px;
    padding: 0 0 0 24px; border-left: 1px solid var(--header-rule);
  }
  .board th:first-child { border-left: none; }
  .board td {
    height: 44px; font-size: 14px; padding: 0 0 0 24px;
    border-left: 1px solid var(--row-rule); vertical-align: middle;
    white-space: nowrap;
  }
  .board td:first-child { border-left: none; }
  .board tbody tr:nth-child(odd) td { background: var(--row-white); }
  .board tbody tr:nth-child(even) td { background: var(--row-alt); }

  .rep-ranking { top: 117px; }
  .rep-ranking th:first-child { padding-left: 14px; }
  .rep-ranking td:first-child { padding-left: 22px; }
  .rep-ranking .num-col { padding-left: 28px; }

  .team-ranking { top: 931px; }
  .team-ranking th:first-child, .team-ranking td:first-child { padding-left: 28px; }
  .team-ranking .num-col { padding-left: 26px; }
</style>
</head>
<body>
  <header class="masthead">
    <div class="car car-left" role="img" aria-label="Red vintage race car number 01"></div>
    <div class="brand-name">QV</div>
    <div class="car car-right" role="img" aria-label="Red vintage race car number 10"></div>
    <div class="issue">
      <p class="issue-date">DECEMBER 20, 2012 <span>ISSUE</span></p>
      <p class="issue-title">Crossing the finish line</p>
    </div>
  </header>

  <table class="board rep-ranking">
    <colgroup>
      <col style="width:72px"><col style="width:278px"><col style="width:269px"><col style="width:145px"><col style="width:114px">
    </colgroup>
    <thead>
      <tr>
        <th>Rank</th>
        <th>Sales Rep Name</th>
        <th>Market</th>
        <th class="num-col">Total<br>MTD</th>
        <th class="num-col">Total<br>Ptc</th>
      </tr>
    </thead>
    <tbody>
      <tr><td>1</td><td>Harwell, Dana M</td><td>Dallas</td><td class="num-col">$20.000</td><td class="num-col">90%</td></tr>
      <tr><td>2</td><td>Harwell, Dana M</td><td>Denver</td><td class="num-col">$20.000</td><td class="num-col">90%</td></tr>
      <tr><td>3</td><td>Lindqvist, Marcus R</td><td>Chicago</td><td class="num-col">$20.000</td><td class="num-col">90%</td></tr>
      <tr><td>4</td><td>Lindqvist, Marcus R</td><td>Lindqvist, Marcus R</td><td class="num-col">$20.000</td><td class="num-col">90%</td></tr>
      <tr><td>5</td><td>Lindqvist, Marcus R</td><td>Lindqvist, Marcus R</td><td class="num-col">$20.000</td><td class="num-col">90%</td></tr>
      <tr><td>6</td><td>Lindqvist, Marcus R</td><td>Lindqvist, Marcus R</td><td class="num-col">$20.000</td><td class="num-col">90%</td></tr>
      <tr><td>7</td><td>Harwell, Dana M</td><td>Dallas</td><td class="num-col">$20.000</td><td class="num-col">90%</td></tr>
      <tr><td>8</td><td>Harwell, Dana M</td><td>Denver</td><td class="num-col">$20.000</td><td class="num-col">90%</td></tr>
      <tr><td>9</td><td>Lindqvist, Marcus R</td><td>Chicago</td><td class="num-col">$20.000</td><td class="num-col">90%</td></tr>
      <tr><td>10</td><td>Lindqvist, Marcus R</td><td>Lindqvist, Marcus R</td><td class="num-col">$20.000</td><td class="num-col">90%</td></tr>
      <tr><td>11</td><td>Lindqvist, Marcus R</td><td>Lindqvist, Marcus R</td><td class="num-col">$20.000</td><td class="num-col">90%</td></tr>
      <tr><td>12</td><td>Lindqvist, Marcus R</td><td>Lindqvist, Marcus R</td><td class="num-col">$20.000</td><td class="num-col">90%</td></tr>
      <tr><td>13</td><td>Harwell, Dana M</td><td>Dallas</td><td class="num-col">$20.000</td><td class="num-col">90%</td></tr>
      <tr><td>14</td><td>Harwell, Dana M</td><td>Denver</td><td class="num-col">$20.000</td><td class="num-col">90%</td></tr>
      <tr><td>15</td><td>Lindqvist, Marcus R</td><td>Chicago</td><td class="num-col">$20.000</td><td class="num-col">90%</td></tr>
      <tr><td>16</td><td>Lindqvist, Marcus R</td><td>Lindqvist, Marcus R</td><td class="num-col">$20.000</td><td class="num-col">90%</td></tr>
    </tbody>
  </table>

  <table class="board team-ranking">
    <colgroup>
      <col style="width:328px"><col style="width:117px"><col style="width:104px"><col style="width:111px"><col style="width:110px"><col style="width:108px">
    </colgroup>
    <thead>
      <tr>
        <th>Team Name<br>and Market Location</th>
        <th class="num-col">MTD<br>Sales</th>
        <th class="num-col">Mtd<br>Ptc</th>
        <th class="num-col">July<br>Points</th>
        <th class="num-col">June<br>Points</th>
        <th class="num-col">Total<br>Points</th>
      </tr>
    </thead>
    <tbody>
      <tr><td>Team Orsini - Denver</td><td class="num-col">$20.000</td><td class="num-col">90%</td><td class="num-col">1</td><td class="num-col">2</td><td class="num-col">3</td></tr>
      <tr><td>Team Orsini - Denver</td><td class="num-col">$20.000</td><td class="num-col">90%</td><td class="num-col">1</td><td class="num-col">2</td><td class="num-col">3</td></tr>
      <tr><td>Team Orsini - Denver</td><td class="num-col">$20.000</td><td class="num-col">90%</td><td class="num-col">1</td><td class="num-col">2</td><td class="num-col">3</td></tr>
      <tr><td>Team Orsini - Denver</td><td class="num-col">$20.000</td><td class="num-col">90%</td><td class="num-col">1</td><td class="num-col">2</td><td class="num-col">3</td></tr>
    </tbody>
  </table>
</body>
</html>
```